CRANDEL'S needs a label design for a Moruga Scorpion Pepper Hot Sauce (5oz bottle)

We need a label for a new company based in south Mississippi called CRANDEL'S. We have a new hot sauce made from Moruga Scorpion Peppers that's very hot yet has "layers of flavor". The sauce is a deep red color in a clear bottle. We are looking for something simple yet different and will stand out. We would like to limit the design to 3 colors.

• wide latin?

```html
<!DOCTYPE html>
<html lang="en">
<head>
<meta charset="utf-8">
<title>CRANDEL'S Hot Sauce Label</title>
<link href="https://fonts.googleapis.com/css2?family=Arimo:wght@400;700&family=PT+Sans:wght@400;700&display=swap" rel="stylesheet">
<style>
  :root {
    --green: #0f9245;
    --red: #a01f24;
    --orange: #fbb040;
    --pepper: #8e1c20;
    --ink: #231f20;
    --maroon: #7a1e1a;
    --white: #ffffff;
  }
  html, body {
    margin: 0;
    padding: 0;
    width: 1200px;
    height: 1000px;
    overflow: hidden;
    background: var(--white);
  }
  .label-sheet { display: block; width: 1200px; height: 1000px; }
  .tagline { font-family: "Arimo", Arial, sans-serif; font-size: 33px; fill: var(--white); letter-spacing: 0.5px; }
  .brand-name { font-family: "Arimo", Arial, sans-serif; font-weight: 700; font-size: 60px; fill: var(--white); }
  .product-name { font-family: "Arimo", Arial, sans-serif; font-size: 36px; fill: #000; }
  .net-weight { font-family: "Arimo", Arial, sans-serif; font-size: 32px; font-weight: 700; fill: var(--white); }
  .nutrition { font-family: "PT Sans", Arial, sans-serif; font-size: 16px; fill: var(--ink); }
  .nutrition .heading { font-weight: 700; fill: var(--maroon); font-size: 16.5px; }
  .nutrition .bold { font-weight: 700; }
  .nutrition .col-head { fill: var(--maroon); }
  .nutrition .accent { fill: var(--red); }
  .nutrition .maker { font-weight: 700; fill: var(--red); font-size: 15.5px; }
</style>
</head>
<body>
<svg class="label-sheet" viewBox="0 0 1200 1000" xmlns="http://www.w3.org/2000/svg">
  <defs>
    <path id="front-outline" d="M80,372 C80,330 110,300 148,300 C162,280 190,268 222,270 C244,257 272,249 306,248 C340,249 368,257 390,270 C422,268 450,280 464,300 C502,300 532,330 532,372 L532,560 C532,600 510,626 470,632 C455,660 422,672 392,668 C370,692 340,710 306,710 C272,710 242,692 220,668 C190,672 157,660 142,632 C102,626 80,600 80,560 Z"/>
    <clipPath id="front-clip"><use href="#front-outline"/></clipPath>
    <path id="tagline-arc" d="M140,400 Q306,276 474,400"/>
  </defs>

  <g class="front-label">
    <g clip-path="url(#front-clip)">
      <rect x="70" y="240" width="470" height="170" fill="var(--green)"/>
      <rect x="70" y="408" width="470" height="310" fill="var(--orange)"/>
    </g>
    <use href="#front-outline" fill="none" stroke="var(--white)" stroke-width="2.5" stroke-dasharray="0.5 5" stroke-linecap="round" transform="translate(306 479) scale(0.955 0.95) translate(-306 -479)"/>
    <rect class="brand-band" x="80" y="408" width="452" height="92" fill="var(--red)"/>

    <text class="tagline"><textPath href="#tagline-arc" startOffset="50%" text-anchor="middle">LAYERS OF FLAVOR</textPath></text>
    <text class="brand-name" x="306" y="476" text-anchor="middle" textLength="412" lengthAdjust="spacingAndGlyphs">CRANDEL'S</text>

    <rect class="pepper-art" role="img" aria-label="Illustration of two red scorpion peppers" x="236" y="506" width="144" height="78" rx="32" fill="var(--pepper)"/>

    <text class="product-name" x="300" y="630" text-anchor="middle">HOT SAUCE</text>
    <text class="net-weight" x="304" y="674" text-anchor="middle">5oz</text>
  </g>

  <g class="back-label">
    <rect x="700" y="266" width="320" height="420" rx="9" fill="var(--orange)"/>
    <rect x="709" y="276" width="302" height="401" rx="8" fill="none" stroke="var(--white)" stroke-width="1"/>

    <g class="nutrition">
      <text class="heading" x="737" y="317">Nutrition Information</text>
      <text x="737" y="339"><tspan class="bold">Serving per package:</tspan> 85</text>
      <text x="737" y="361"><tspan class="bold">Serving size:</tspan> 1g or 1/4 tsp</text>

      <text class="col-head" x="857" y="384" text-anchor="middle">Per Serving</text>
      <text class="col-head" x="950" y="384" text-anchor="middle">Per 100 g</text>

      <text x="737" y="405">Energy</text><text x="866" y="405" text-anchor="middle">10kJ</text><text x="949" y="405" text-anchor="middle">1000 kJ</text>
      <text x="737" y="427">Protein</text><text x="866" y="427" text-anchor="middle">0.1g</text><text x="955" y="427" text-anchor="middle">10.4 g</text>
      <text x="752" y="448"><tspan class="accent">*</tspan>Gluten Not detected....................</text>
      <text x="737" y="470">Fat, total</text><text x="866" y="470" text-anchor="middle">0.1g</text><text x="955" y="470" text-anchor="middle">10.0 g</text>
      <text x="737" y="492"><tspan class="accent">*</tspan>Saturated</text><text x="866" y="492" text-anchor="middle">0.0g</text><text x="958" y="492" text-anchor="middle">0.9 g</text>
      <text x="737" y="514">Carbohydrate</text><text x="866" y="514" text-anchor="middle">0.4g</text><text x="955" y="514" text-anchor="middle">36.2 g</text>
      <text x="737" y="536"><tspan class="accent">*</tspan>Sugar</text><text x="866" y="536" text-anchor="middle">0.0g</text><text x="958" y="536" text-anchor="middle">3.4 g</text>
      <text x="737" y="557">Sodium</text><text x="866" y="557" text-anchor="middle">111mg</text><text x="946" y="557" text-anchor="middle">11100mg</text>

      <text x="737" y="601"><tspan class="maker">Ingredients:</tspan>Lorem ipsum dolor sit</text>
      <text x="737" y="622">amet, mauris tristique</text>

      <text class="maker" x="737" y="658">DIST &amp; SOLD BY CRANDEL'S, MS</text>
    </g>
  </g>
</svg>
</body>
</html>
```